Biz Cards for Velmora Associates

Velmora Associates is seeking a single-sided business card that is more visually-appealing than our current design (see attached).

Notes:
- Our colors are blue & teal.
- Our tag line must be large enough to be easily read
- We don't necessarily need our address included (that's just the biz office)
- We'd like to add our email address: Velmora417@quillbox.net

Thanks!

Industry/Entity Type

Business

Contact Information for Business Card

Standard size
PSD file required w/ text on its own layer

Colors
86cfc6
3277b5

```html
<!DOCTYPE html>
<html lang="en">
<head>
<meta charset="utf-8">
<title>Velmora Associates – Business Cards</title>
<link href="https://fonts.googleapis.com/css2?family=Roboto:ital,wght@0,400;0,500;1,400&display=swap" rel="stylesheet">
<style>
  :root {
    --stage: #e9e6e2;
    --blue-deep: #0f63b0;
    --blue: #3277b5;
    --teal: #86cfc6;
    --teal-glow: #3fa9bd;
    --panel: #f4f6f8;
    --ink: #2a2a2c;
    --card-dark: #29282b;
    --white: #ffffff;
    --tagline: #2a6fb8;
    --arc: #1e1c1d;
  }
  * { margin: 0; padding: 0; box-sizing: border-box; }
  html, body { width: 1200px; height: 960px; overflow: hidden; }
  body {
    background: var(--stage);
    font-family: "Roboto", Arial, sans-serif;
    position: relative;
  }
  .card {
    position: absolute;
    width: 600px;
    height: 343px;
    overflow: hidden;
    box-shadow: 0 3px 8px rgba(0,0,0,0.25);
  }
  .card-front {
    left: 314px; top: 113px;
    background: radial-gradient(circle at 40% 55%, var(--teal-glow) 0%, #1f86c4 30%, var(--blue-deep) 75%);
  }
  .card-front .panel { position: absolute; inset: 0; }
  .holder {
    position: absolute; left: 39px; top: 44px; color: var(--white);
  }
  .holder-name { font-size: 20px; font-weight: 500; letter-spacing: -0.2px; }
  .holder-title { font-size: 15px; margin-top: 3px; }
  .contacts {
    position: absolute; left: 40px; top: 231px; list-style: none; color: var(--white);
    font-size: 14px;
  }
  .contacts li { display: flex; align-items: center; height: 18.5px; }
  .contacts svg { width: 13px; height: 13px; margin-right: 9px; fill: var(--white); }
  .brand {
    position: absolute; left: 300px; top: 157px; width: 270px;
    display: flex; align-items: center; justify-content: center; gap: 10px;
  }
  .brand-dot { width: 20px; height: 20px; border-radius: 50%; background: var(--blue); flex: none; }
  .brand-name { font-size: 24px; font-weight: 400; color: var(--ink); letter-spacing: 0.5px; white-space: nowrap; }
  .tagline { font-style: italic; color: var(--tagline); white-space: nowrap; }
  .card-front .tagline {
    position: absolute; left: 300px; width: 270px; top: 214px; text-align: center; font-size: 11.5px;
  }
  .card-back { left: 311px; top: 472px; background: var(--card-dark); }
  .card-back .brand-mark {
    position: absolute; left: 0; right: 0; top: 128px;
    display: flex; align-items: center; justify-content: center; gap: 12px;
  }
  .card-back .brand-dot { width: 28px; height: 28px; background: var(--teal); }
  .card-back .brand-name { color: var(--white); font-size: 30px; }
  .card-back .tagline {
    position: absolute; left: 0; right: 0; top: 265px; text-align: center; font-size: 13px;
  }
  .website {
    position: absolute; left: 0; right: 0; top: 288px; text-align: center;
    color: var(--white); font-size: 14px; letter-spacing: 3px;
  }
</style>
</head>
<body>
  <section class="card card-front">
    <svg class="panel" viewBox="0 0 600 343" width="600" height="343" aria-hidden="true">
      <path d="M 352 0 C 236 60 226 290 380 343 L 600 343 L 600 0 Z" fill="var(--panel)"/>
      <path d="M 352 0 C 236 60 226 290 380 343" fill="none" stroke="var(--arc)" stroke-width="6"/>
    </svg>
    <div class="holder">
      <p class="holder-name">Dana Whitfield, RN</p>
      <p class="holder-title">Mental Health Therapist</p>
    </div>
    <ul class="contacts">
      <li><svg viewBox="0 0 16 16"><path d="M3.6 1.2l2.3 2.6-1.2 1.9c.9 2 2.6 3.7 4.6 4.6l1.9-1.2 2.6 2.3-1 2.4C7.6 14 2 8.4 1.2 2.2z"/></svg>(855) VELM-ORA</li>
      <li><svg viewBox="0 0 16 16"><path d="M4 1h8v4H4zM1 6h14v6h-3v3H4v-3H1zM5 10v4h6v-4z"/></svg>(330) 555-0182</li>
      <li><svg viewBox="0 0 16 16"><path d="M1 3h14v1L8 9 1 4zM1 6l7 5 7-5v7H1z"/></svg>Velmora417@quillbox.net</li>
      <li><svg viewBox="0 0 16 16"><path d="M8 1a7 7 0 100 14A7 7 0 008 1zm-1 2.2c-.6 1-1.6 1.2-2 2.4.8.3 1.8 0 2.2 1-.6 1-2 1.2-1.4 2.6 1 .4 1 2 1.2 3.6A5.2 5.2 0 017 3.2zm3 1c1 .8 2.6 2 2.8 3.8-1.2 0-1.8-1-2.8-.6-.6-1-1-1.8 0-3.2z"/></svg>VelmoraAssoc.net</li>
    </ul>
    <div class="brand">
      <span class="brand-dot"></span>
      <span class="brand-name">Velmora Associates</span>
    </div>
    <p class="tagline">Thoughtful Care. Steady Hands. Brighter days.</p>
  </section>

  <section class="card card-back">
    <div class="brand-mark">
      <span class="brand-dot"></span>
      <span class="brand-name">Velmora Associates</span>
    </div>
    <p class="tagline">Thoughtful Care. Steady Hands. Brighter days.</p>
    <p class="website">www.VelmoraAssoc.net</p>
  </section>
</body>
</html>
```